Marta Belle Designs & Events business card

I need an elegant informative but not busy business card using my logo. We are a florist with high end customers. I am adding a PDF file and a PNG file for those who requested it
Updates

Target Market(s)

Brides, grooms, men purchasing flowers
Ages 20-65

Industry/Entity Type

Florist

Requirements
Must have
• Business info:
Marta Belle Design & Events
www.martabelleevents-sample.com.
555-418-2763

555-418-2763
Nice to have
• Est 1954
may want Pinterest logo, twitter and linkedin and facbook
Should not have
• Clip art or photos

```html
<!DOCTYPE html>
<html lang="en">
<head>
<meta charset="utf-8">
<title>Marta Belle Designs &amp; Events — Business Card</title>
<link rel="stylesheet" href="https://fonts.googleapis.com/css2?family=Marcellus&family=Marcellus+SC&family=Cabin:wght@400&display=swap">
<style>
  :root {
    --backdrop: #151515;
    --card-white: #ffffff;
    --ink: #1c1c1c;
    --blush: #f3b3c1;
    --blush-light: #f7c7d2;
    --blush-deep: #e98aa1;
    --border-white: #ffffff;
  }
  * { box-sizing: border-box; margin: 0; padding: 0; }
  html, body {
    width: 1200px;
    height: 873px;
    overflow: hidden;
    background: var(--backdrop);
  }
  .sheet {
    width: 1200px;
    height: 873px;
    display: flex;
    align-items: center;
    justify-content: center;
    gap: 60px;
  }
  .card {
    width: 525px;
    height: 300px;
    position: relative;
    box-shadow: 0 10px 30px rgba(0,0,0,0.5);
  }

  /* Front */
  .card-front {
    background: var(--card-white);
    color: var(--ink);
    padding: 34px 40px 0 96px;
  }
  .brand {
    display: flex;
    align-items: center;
    justify-content: center;
    gap: 10px;
    margin-left: 40px;
  }
  .brand-dot {
    width: 12px;
    height: 12px;
    border-radius: 50%;
    background: var(--blush-deep);
  }
  .brand-name {
    font-family: "Marcellus", serif;
    font-size: 17px;
    letter-spacing: 0.18em;
    text-transform: uppercase;
    color: var(--ink);
  }
  .company {
    margin-top: 34px;
    font-family: "Marcellus SC", serif;
    font-size: 21px;
    letter-spacing: 0.03em;
    color: var(--ink);
  }
  .contact {
    list-style: none;
    margin-top: 12px;
    font-family: "Cabin", sans-serif;
    font-size: 14px;
    line-height: 1.6;
    color: var(--ink);
  }

  /* Back */
  .card-back {
    background: var(--border-white);
    padding: 9px;
  }
  .back-field {
    width: 100%;
    height: 100%;
    position: relative;
    display: flex;
    align-items: center;
    justify-content: center;
  }
  .back-pattern {
    position: absolute;
    inset: 0;
    background: radial-gradient(circle at 50% 50%, var(--blush-light), var(--blush) 70%);
  }
  .back-name {
    position: relative;
    font-family: "Marcellus", serif;
    font-size: 20px;
    letter-spacing: 0.14em;
    text-transform: uppercase;
    color: var(--ink);
  }
</style>
</head>
<body>
  <main class="sheet">
    <section class="card card-front" aria-label="Business card front">
      <div class="brand">
        <span class="brand-dot"></span>
        <span class="brand-name">Marta Belle Designs &amp; Events</span>
      </div>
      <h1 class="company">Marta Belle Design &amp; Events</h1>
      <ul class="contact">
        <li>www.martabelleevents-sample.com</li>
        <li>555-418-2763</li>
        <li>Est. 1954</li>
      </ul>
    </section>

    <section class="card card-back" aria-label="Business card back">
      <div class="back-field">
        <div class="back-pattern" role="img" aria-label="Soft pink field with a faint tonal floral scroll pattern"></div>
        <span class="back-name">Marta Belle Designs &amp; Events</span>
      </div>
    </section>
  </main>
</body>
</html>
```